Harbor Nightclub

Nightclub flyer., digital single sided, for KV and PX. I included samples of some previous flyers we've used. Sample Info:
HARBOR
FRIDAYS
FRI MAY 1 2020
DJ VORTAN (club floor)
DJ RUZO & DJ TAV (residents on the lounge floor)
4217 Marlow Avenue Sacramento
www.harborvenuehall.example for list/VIP inquiries

Target Market(s)

Upscale top 40 crowd but want some cool and artsy like the examples included.

Font styles to use
Sans Serif

Requirements
Must have
• Harbor Logo
Nice to have
• Would be nice if the flyer can be incorporated later with DJ photos (sometimes we will add dj photos to pixagram etc). Would like a big city type of feel.
Should not have
• Nothing too sexual.

```html
<!DOCTYPE html>
<html lang="en">
<head>
<meta charset="utf-8">
<title>Harbor Nightclub – Fridays Flyer</title>
<link rel="stylesheet" href="https://fonts.googleapis.com/css2?family=Bebas+Neue&family=Montserrat:wght@300&family=Playfair+Display:wght@400&display=swap">
<style>
  :root {
    --page-bg: #ffffff;
    --night-black: #04060a;
    --night-navy: #0b1728;
    --sky-haze: #1d2a44;
    --river-blue: #1a5f86;
    --glow-teal: #2fb6d8;
    --tower-green: #3fa58a;
    --signal-red: #d8304f;
    --city-violet: #3a2a6a;
    --figure-dark: #0a0f18;
    --text-white: #ffffff;
    --text-blush: #f4dcef;
    --badge-green: #6a9a3c;
  }
  html, body {
    margin: 0;
    width: 1200px;
    height: 1200px;
    overflow: hidden;
    background: var(--page-bg);
  }
  .flyer {
    position: absolute;
    left: 219px;
    top: 65px;
    width: 754px;
    height: 1063px;
    background: var(--night-black);
    overflow: hidden;
    color: var(--text-white);
    font-family: "Bebas Neue", "Oswald", sans-serif;
    box-shadow: 4px 4px 8px rgba(0,0,0,0.35);
  }
  .flyer-photo {
    position: absolute;
    inset: 0;
    background:
      /* performer silhouette zone, centre */
      radial-gradient(ellipse 22% 14% at 50% 22%, rgba(120,110,130,0.55) 0%, transparent 100%),
      radial-gradient(ellipse 28% 40% at 51% 48%, var(--figure-dark) 0%, rgba(10,15,24,0.85) 55%, transparent 100%),
      /* skyline glow, left */
      radial-gradient(ellipse 22% 18% at 20% 40%, rgba(63,165,138,0.55) 0%, transparent 100%),
      radial-gradient(circle at 10% 29%, rgba(216,48,79,0.7) 0%, transparent 4%),
      radial-gradient(circle at 25% 22%, rgba(216,48,79,0.6) 0%, transparent 3%),
      radial-gradient(circle at 17% 40%, rgba(255,255,255,0.55) 0%, transparent 3%),
      radial-gradient(ellipse 18% 12% at 12% 49%, rgba(230,210,200,0.4) 0%, transparent 100%),
      /* skyline glow, right */
      radial-gradient(ellipse 14% 20% at 89% 33%, rgba(90,200,190,0.55) 0%, transparent 100%),
      radial-gradient(ellipse 10% 8% at 70% 30%, rgba(80,90,200,0.45) 0%, transparent 100%),
      radial-gradient(circle at 78% 36%, rgba(216,48,79,0.75) 0%, transparent 4%),
      radial-gradient(ellipse 26% 5% at 88% 44%, rgba(140,200,255,0.5) 0%, transparent 100%),
      /* river reflections */
      radial-gradient(ellipse 30% 10% at 12% 55%, rgba(70,90,220,0.45) 0%, transparent 100%),
      radial-gradient(ellipse 26% 10% at 88% 53%, rgba(110,70,200,0.45) 0%, transparent 100%),
      /* diagonal light streaks */
      linear-gradient(152deg, transparent 56%, rgba(47,182,216,0.45) 63%, transparent 69%),
      linear-gradient(152deg, transparent 64%, rgba(26,95,134,0.55) 70%, transparent 78%),
      linear-gradient(152deg, transparent 46%, rgba(47,182,216,0.2) 52%, transparent 58%),
      linear-gradient(180deg, #070b14 0%, var(--night-navy) 12%, var(--sky-haze) 24%, #1b2a48 36%, #1c3a66 46%, #143a5a 56%, #0b1a2a 70%, var(--night-black) 86%);
  }
  .brand-mark {
    position: absolute;
    left: 514px;
    top: 32px;
    width: 214px;
    text-align: center;
  }
  .brand-mark .badge {
    display: block;
    width: 92px;
    height: 92px;
    margin: 0 auto 14px;
    border-radius: 50%;
    background: var(--badge-green);
  }
  .brand-mark .brand-name {
    font-family: "Playfair Display", serif;
    font-size: 42px;
    line-height: 1;
    color: var(--text-white);
    letter-spacing: 4px;
  }
  .event-title {
    position: absolute;
    left: 0;
    right: 0;
    top: 556px;
    margin: 0;
    text-align: center;
    font-size: 218px;
    line-height: 1;
    font-weight: 400;
    letter-spacing: 2px;
    color: var(--text-white);
    text-shadow: 2px 2px 0 var(--glow-teal);
  }
  .event-date {
    position: absolute;
    left: 0;
    right: 0;
    top: 744px;
    text-align: center;
    font-family: "Montserrat", sans-serif;
    font-weight: 300;
    font-size: 46px;
    line-height: 1;
  }
  .venue-address {
    position: absolute;
    left: 0;
    right: 0;
    top: 834px;
    text-align: center;
    font-size: 30px;
    line-height: 1;
    letter-spacing: 5px;
    color: var(--text-blush);
  }
  .divider {
    position: absolute;
    left: 116px;
    width: 522px;
    height: 2px;
    background: var(--text-blush);
  }
  .divider.top { top: 873px; }
  .divider.bottom { top: 968px; }
  .lineup {
    position: absolute;
    left: 0;
    right: 0;
    top: 885px;
    margin: 0;
    padding: 0;
    list-style: none;
    text-align: center;
    font-size: 31px;
    line-height: 37px;
    color: var(--text-blush);
  }
  .guest-list {
    position: absolute;
    left: 0;
    right: 0;
    top: 1000px;
    text-align: center;
    font-size: 27px;
    line-height: 1;
    letter-spacing: 1.6px;
    color: var(--text-blush);
  }
</style>
</head>
<body>
  <main class="flyer">
    <div class="flyer-photo" role="img" aria-label="Night city skyline along a river with lit towers, a DJ wearing headphones in the foreground and blue light streaks"></div>

    <div class="brand-mark">
      <span class="badge"></span>
      <div class="brand-name">HARBOR</div>
    </div>

    <h1 class="event-title">HARBOR</h1>
    <div class="event-date">FRI MAY 1 2020</div>

    <div class="venue-address">4217 Marlow Avenue Sacramento</div>
    <div class="divider top"></div>
    <ul class="lineup">
      <li>DJ VORTAN (CLUB FLOOR)</li>
      <li>DJ RUZO &amp; DJ TAV (RESIDENTS ON THE LOUNGE FLOOR)</li>
    </ul>
    <div class="divider bottom"></div>
    <div class="guest-list">WWW.HARBORVENUEHALL.EXAMPLE FOR LIST/VIP INQUIRIES</div>
  </main>
</body>
</html>
```